Corporate brochure Velorin consulting

I am a business law and taxation law firm. I would like to create a super sharp and modern catalogue that really describes our values and the services we offer among other things. It has to be bilingual. I dont want it to look like old fashioned typical law firms. Here are some characteristics of the catalogue:

- size: 8.5 x 11 landscape
- 20 pages in total including the cover page
- bilingual catalogue

Our corporate colors are the ones used in the logo attached.

I already have purchased all of the photos needed for the project.Please see attached document for a detailed description of the project.

I have pictures that I can email you for the project. just email me at jbarlow@velorin-example.ca and I will send the file.

I would just like for you to make available the text boxes on each page and then I will provide the text once Im finished.

Target Market(s)

business owners and professionals

Industry/Entity Type

Business

Font styles to use
Sans Serif

Colors
0692cd
f37122

Requirements
Must have
• bold fonts, very clean white backgrounds, modern and yet very edgy design
• each page should have a large enough area to add text.
• ***I like as the titles: all in large letters and font to use is Adequate,
• Large titles on the left side of page in orange and right side in blue
• for the text: font to be used is asenine
• page numbering should be very visible in the middle of the page left and right and not on bottom or upper corners.
Nice to have
• I like the use of metallic silvers . Not all of the pictures need to be used its the choic of the designer.

```html
<!DOCTYPE html>
<html lang="en">
<head>
<meta charset="utf-8">
<title>Velorin Consulting – Services spread</title>
<link href="https://fonts.googleapis.com/css2?family=Oswald:wght@400;500&family=Open+Sans:wght@400;600;700&display=swap" rel="stylesheet">
<style>
  :root{
    --blue:#0692cd;
    --orange:#f37122;
    --charcoal:#3a3a3a;
    --text:#555a5e;
    --paper:#ffffff;
    --backdrop:#e4e5e7;
  }
  *{box-sizing:border-box;margin:0;padding:0}
  html,body{width:1200px;height:638px;overflow:hidden;background:var(--backdrop)}
  body{font-family:"Open Sans",Arial,sans-serif;color:var(--text)}
  .spread{position:absolute;left:30px;top:95px;width:1140px;height:448px;display:flex;background:var(--paper);box-shadow:0 6px 24px rgba(0,0,0,.12)}
  .page{position:relative;width:570px;height:448px;overflow:hidden}
  .page--left{border-right:1px solid #e2e2e2}
  .hero{position:absolute;left:0;top:0;width:100%;height:122px}
  .hero--sky{background:linear-gradient(100deg,#b9dcf2 0%,#d9b79f 30%,#6fb3e0 55%,#3f9fd9 100%)}
  .hero--house{background:linear-gradient(90deg,#f4f3f1 0%,#dcc8b8 35%,#e8a886 55%,#6f7178 75%,#eeeeee 100%)}
  .tag{position:absolute;top:0;background:var(--charcoal);color:#fff;font:600 9px "Open Sans",sans-serif;letter-spacing:.5px;padding:6px 9px}
  .page--left .tag{left:30px}
  .page--right .tag{right:30px}
  .banner{position:absolute;top:70px;height:34px;background:var(--orange);color:#fff;font:400 21px/34px "Oswald",sans-serif;text-transform:uppercase;letter-spacing:.3px}
  .page--left .banner{left:0;padding:0 16px 0 30px}
  .page--right .banner{left:0;padding:0 16px 0 12px}
  .content{position:absolute;top:138px;left:30px;right:30px}
  .page--right .content{left:26px;right:34px}
  .intro{font-size:6.4px;line-height:1.5;margin-bottom:9px}
  .section h2{font:700 8.6px/1.2 "Open Sans",sans-serif;text-transform:uppercase;margin-bottom:2px}
  .section p{font-size:6.4px;line-height:1.5;margin-bottom:4px}
  .section{margin-bottom:5px}
  .page--left .section:nth-of-type(odd) h2{color:var(--blue)}
  .page--left .section:nth-of-type(even) h2{color:var(--orange)}
  .page--right .section h2{color:var(--orange)}
  .footer{position:absolute;left:0;bottom:0;width:100%;height:44px;background:var(--orange);display:flex;align-items:center;color:#fff}
  .footer__rule{flex:1;height:1px;background:rgba(255,255,255,.7)}
  .page-number{width:26px;height:26px;border-radius:50%;background:#fff;color:var(--charcoal);font:700 10px/26px "Open Sans",sans-serif;text-align:center;flex:none}
  .footer__line{font:600 6.4px "Open Sans",sans-serif;white-space:nowrap;padding:0 10px;flex:none}
  .footer__line b{font-weight:700}
  .brand{font:700 10px "Open Sans",sans-serif;letter-spacing:1px;flex:none}
  .page--left .footer{padding:0 18px 0 30px}
  .page--left .page-number{margin-right:14px}
  .page--left .brand{margin-left:14px}
  .page--right .footer{padding:0 30px 0 18px}
  .page--right .brand{margin-right:14px}
  .page--right .page-number{margin-left:14px}
</style>
</head>
<body>
<main class="spread">
  <section class="page page--left">
    <div class="hero hero--sky" role="img" aria-label="Cupped hands sheltering a blue paper house with a family cut-out and a red heart against a blue sky"></div>
    <span class="tag">SERVICES</span>
    <h1 class="banner">Asset Protection</h1>
    <div class="content">
      <p class="intro">In case of litigation or legal disputes, our lawyers can help protect your personal assets against seizure by a potential creditor.</p>
      <div class="section">
        <h2>Incorporation</h2>
        <p>A corporation possesses its own legal personality separate from that of its shareholders. By shielding personal assets from a corporation's creditors, shareholders obtain asset protection and peace of mind while running a business.</p>
      </div>
      <div class="section">
        <h2>Holding Corporation</h2>
        <p>This strategy allows for the separation of a corporation's activities into two separate entities: the operating company and the holding company. The operating company handles day-to-day operations of the business while the holding company contains the business' investments and excess cash. In case of a lawsuit, assets found in the holding company can be protected from court claims.</p>
      </div>
      <div class="section">
        <h2>Loans between corporations guaranteed by a moveable hypothec</h2>
        <p>This strategy allows for the operating company's assets to be protected in case of a legal action. Instead of borrowing money from a bank, the operating company borrows working capital from the holding company. In exchange, the operating company grants a hypothec on the universality of its property (trucks, equipment etc.) in favour of the holding company.</p>
        <p>Given that the holding company has a hypothec on the property of the operating company, the property of the latter is protected from seizure by creditors. This is because the hypothec held by the holding company would rank ahead of any other creditor's rank.</p>
      </div>
      <div class="section">
        <h2>Asset protection trust ( or principal residence trust)</h2>
        <p>This inter vivos trust is created by drafting a private document and then transferring valuable real real estate into it such as a principal residence. Since a trust has a separate legal personality distinct from the person who created it, should a lawsuit occur, creditors will not be able to seize property held in the trust.</p>
      </div>
    </div>
    <footer class="footer">
      <span class="page-number">14</span>
      <span class="footer__rule"></span>
      <span class="footer__line"><b>VELORIN CONSULTING</b> - A Creative Law Firm</span>
      <span class="footer__rule"></span>
      <span class="brand">VELORIN</span>
    </footer>
  </section>

  <section class="page page--right">
    <div class="hero hero--house" role="img" aria-label="Two hands held protectively over a small model house with an orange facade and grey roof"></div>
    <span class="tag">SERVICES</span>
    <h1 class="banner">Protection d'actifs</h1>
    <div class="content">
      <p class="intro">En cas de poursuites, nous pouvons vous aider à protéger vos biens personnels contre vos créanciers par la mise en place de certaines stratégies légales :</p>
      <div class="section">
        <h2>L'incorporation</h2>
        <p>La société par actions dispose d'un patrimoine distinct de son actionnaire, ce qui protège ce dernier, parce qu'il n'a pas à rembourser personnellement les dettes de sa société. Par conséquent, ses biens personnels sont généralement à l'abri des créanciers.</p>
      </div>
      <div class="section">
        <h2>La société de gestion (ou de portefeuille)</h2>
        <p>Cette stratégie permet de séparer, par l'entremise d'une société par actions distinctes, les activités courantes de la société par action opérante des investissements de l'actionnaire (portefeuille d'actions, fonds mutuels, immobilier).</p>
      </div>
      <div class="section">
        <h2>Le prêt entre sociétés garanti par hypothèque</h2>
        <p>Cette stratégie vise à protéger les biens de la société opérante en cas de poursuites. Au lieu d'emprunter de l'argent à une banque, la société opérante emprunte à la société de gestion les liquidités du fonds de roulement. En échange, la société de gestion enregistre une hypothèque universelle sur les biens de la société opérante (camions, équipements, etc.).</p>
        <p>Étant donné que la société de gestion détient une hypothèque sur l'universalité des biens de la société opérante, les biens de cette dernière sont protégés contre ses créanciers, parce que la dette de la société de gestion est prioritaire à celle des autres créanciers.</p>
      </div>
      <div class="section">
        <h2>La fiducie de protection d'actifs</h2>
        <p>Cette fiducie entre vifs est créée suite à la rédaction d'un document juridique sous seing privé. Elle possède un patrimoine juridique distinct de l'entrepreneur. Généralement, en cas de poursuites, les créanciers ne pourront pas avoir accès aux biens détenus par la fiducie.</p>
      </div>
    </div>
    <footer class="footer">
      <span class="brand">VELORIN</span>
      <span class="footer__rule"></span>
      <span class="footer__line"><b>VELORIN CONSULTING</b> - A Creative Law Firm</span>
      <span class="footer__rule"></span>
      <span class="page-number">15</span>
    </footer>
  </section>
</main>
</body>
</html>
```